Business Card for Freelance Copywriting & Web Design Business

Hi! I have a logo but want a new business card. Here's a better idea of what I'm thinking:
-Brand new double-sided business card, rounded cards, embossed logo, nice quality paper
-Include phone (604-382-5194), email (hello@lauraberndt.org), and website (www.lauraberndt.org). No address, please, since I service clients worldwide.
-I'd like the fonts to match those on my website (www.lauraberndt.org). I had to purchase the one font (Born Ready), attached. I'm not sure which version was used on my site so I included all that I purchased. The secondary font is Helvetica
-I'd also like the tagline "Powerful Words. Impressive Results." included.
-My primary brand colour is the teal, colour #19ADC3
Laura Berndt | Laura Berndt Copywriting & Web Design <hello@lauraberndt.org>
-I'd also like the following services listed on the new cards:
SEO Website Content
SEO Blog Content
SEO Website Design
Contact Information for Business Card
as stated in brief
Font styles to use
Other font styles liked:
- See brief
Look and feel
Each slider illustrates characteristics of the customer's brand and the style your logo design should communicate.

```html
<!DOCTYPE html>
<html lang="en">
<head>
<meta charset="utf-8">
<title>Laura Berndt – Business Card</title>
<link href="https://fonts.googleapis.com/css2?family=Arimo:wght@400;700&display=swap" rel="stylesheet">
<style>
  :root {
    --teal: #19adc3;
    --teal-deep: #109fb6;
    --teal-light: #8fd3de;
    --ink: #111111;
    --paper: #ffffff;
    --backdrop: #cfd3d4;
  }
  * { box-sizing: border-box; margin: 0; padding: 0; }
  html, body { width: 1200px; height: 960px; overflow: hidden; }
  body {
    background: var(--backdrop);
    font-family: "Arimo", Helvetica, Arial, sans-serif;
    position: relative;
  }
  .card {
    position: absolute;
    top: 105px;
    width: 430px;
    height: 750px;
    border-radius: 30px;
    overflow: hidden;
    box-shadow: 0 10px 28px rgba(0,0,0,0.35);
  }
  .card--front { left: 142px; background: var(--teal-deep); }
  .card--front svg { display: block; }
  .card--back {
    left: 632px;
    width: 428px;
    background: var(--paper);
    border: 5px solid var(--teal);
  }
  .back-mark {
    position: absolute;
    left: 0; right: 0; top: 0;
    height: 210px;
  }
  .back-mark__art {
    position: absolute;
    left: 150px; top: 30px;
    width: 200px; height: 170px;
    border-radius: 50%;
    background: radial-gradient(ellipse at 55% 45%, rgba(143,211,222,0.75), rgba(143,211,222,0) 70%);
  }
  .back-mark__name {
    position: absolute;
    left: 0; right: 0; top: 86px;
    text-align: center;
    font-size: 40px;
    font-weight: 400;
    color: var(--ink);
  }
  .back-mark__line {
    position: absolute;
    left: 0; right: 0; top: 143px;
    text-align: center;
    font-size: 13px;
    font-weight: 700;
    letter-spacing: 2.4px;
    color: var(--ink);
  }
  .contact__name {
    position: absolute;
    left: 0; right: 0; top: 425px;
    text-align: center;
    font-size: 35px;
    font-weight: 700;
    color: var(--teal);
  }
  .contact__role {
    position: absolute;
    left: 0; right: 0; top: 469px;
    text-align: center;
    font-size: 18px;
    color: var(--ink);
  }
  .contact__icons {
    position: absolute;
    left: 95px; top: 498px;
    width: 236px; height: 40px;
  }
  .contact__list {
    position: absolute;
    left: 0; right: 0; top: 545px;
    list-style: none;
    text-align: center;
    font-size: 17px;
    line-height: 25px;
    color: var(--ink);
  }
  .rule {
    position: absolute;
    left: 95px; top: 638px;
    width: 231px; height: 2px;
    background: var(--teal);
  }
  .tagline {
    position: absolute;
    left: 0; right: 0; top: 656px;
    text-align: center;
    font-size: 18px;
    line-height: 24px;
    color: var(--ink);
  }
</style>
</head>
<body>

<section class="card card--front" aria-label="Card front">
  <svg width="430" height="750" viewBox="0 0 430 750" xmlns="http://www.w3.org/2000/svg">
    <defs>
      <radialGradient id="embossGlow" cx="45%" cy="45%" r="70%">
        <stop offset="0" stop-color="#1fb6cc"/>
        <stop offset="1" stop-color="#0fa0b6"/>
      </radialGradient>
      <radialGradient id="featherGlow" cx="50%" cy="45%" r="55%">
        <stop offset="0" stop-color="#ffffff" stop-opacity="0.95"/>
        <stop offset="0.6" stop-color="#ffffff" stop-opacity="0.45"/>
        <stop offset="1" stop-color="#ffffff" stop-opacity="0"/>
      </radialGradient>
    </defs>
    <rect class="front-emboss" width="430" height="750" fill="url(#embossGlow)" role="img" aria-label="Large embossed feather pattern across the card"/>
    <ellipse class="front-feather" cx="200" cy="360" rx="120" ry="210" transform="rotate(28 200 360)" fill="url(#featherGlow)" role="img" aria-label="White feather illustration"/>
    <g fill="var(--ink)" font-family="Arimo, Helvetica, Arial, sans-serif">
      <text class="front-name" transform="translate(205 368) rotate(-90)" text-anchor="middle" font-size="58">Laura Berndt</text>
      <text class="front-line" transform="translate(274 351) rotate(-90)" text-anchor="middle" font-size="19" font-weight="700" letter-spacing="3">COPYWRITING &amp; WEB DESIGN</text>
    </g>
    <g fill="#ffffff" font-family="Arimo, Helvetica, Arial, sans-serif">
      <text class="front-services-title" transform="translate(369 440) rotate(-90)" font-size="20">SERVICES</text>
      <text class="front-services" transform="translate(393 684) rotate(-90)" font-size="16.5">• SEO Website Content  • SEO Blog Content  • SEO Website Design</text>
    </g>
  </svg>
</section>

<section class="card card--back" aria-label="Card back">
  <div class="back-mark">
    <div class="back-mark__art" role="img" aria-label="Soft teal feather illustration"></div>
    <div class="back-mark__name">Laura Berndt</div>
    <div class="back-mark__line">COPYWRITING &amp; WEB DESIGN</div>
  </div>

  <h1 class="contact__name">Laura Berndt</h1>
  <p class="contact__role">Copywriting &amp; Web Design</p>

  <svg class="contact__icons" viewBox="0 0 236 40" xmlns="http://www.w3.org/2000/svg" aria-hidden="true">
    <g stroke="var(--teal)" stroke-width="2">
      <line x1="5" y1="20" x2="61" y2="20"/>
      <line x1="176" y1="20" x2="231" y2="20"/>
    </g>
    <g fill="var(--teal)">
      <rect x="68" y="5" width="22" height="22" rx="4" transform="rotate(45 79 20) translate(0 4)"/>
      <rect x="107" y="5" width="22" height="22" rx="4" transform="rotate(45 118 20) translate(0 4)"/>
      <rect x="146" y="5" width="22" height="22" rx="4" transform="rotate(45 157 20) translate(0 4)"/>
    </g>
    <path d="M74 14 q-1 8 8 12 l2-3 -3-2 -2 1 q-3-2-4-5 l1-2 -2-3z" fill="#fff"/>
    <g fill="none" stroke="#fff" stroke-width="1.5">
      <rect x="112" y="15" width="12" height="9" rx="1"/>
      <polyline points="112,15 118,20 124,15"/>
      <circle cx="157" cy="20" r="6.5"/>
      <ellipse cx="157" cy="20" rx="2.8" ry="6.5"/>
      <line x1="150.5" y1="20" x2="163.5" y2="20"/>
    </g>
  </svg>

  <ul class="contact__list">
    <li>(604-382-5194)</li>
    <li>www.lauraberndt.org</li>
    <li>hello@lauraberndt.org</li>
  </ul>

  <div class="rule"></div>

  <p class="tagline">Powerful Words.<br>Impressive Results.</p>
</section>

</body>
</html>
```